Individual Ice Cream cup poster for retailers

I need an A5 round Point of Sale poster scaleable down to an A4 size for retailers of our 125ml 'dixie' cup ice cream flavours. This poster needs to reflect the quality of our product but yet be playful and colorful too. It needs to speak 'farm fresh' as well.
"spoon inside' needs to indicated too please.

Target Market(s)

ice cream onsumers in confined food retail space

Industry/Entity Type

Manufacturer

Font styles to use
Sans Serif

Colors
acd036

Requirements
Must have
• A5 size and A4 size but oval/round in shape
• A white block out round space for the retailer to mark their rec retail price
Nice to have
• Brighter colours than in the images supplied
Should not have
• a cheap feel

```html
<!DOCTYPE html>
<html lang="en">
<head>
<meta charset="utf-8">
<title>Kelburn Fine Ice Cream – Cup Point of Sale</title>
<link href="https://fonts.googleapis.com/css2?family=Rubik:wght@800&display=swap" rel="stylesheet">
<style>
  :root {
    --paper: #ffffff;
    --ink: #111111;
    --leaf: #7fbf3f;
    --lime: #acd036;
    --lime-soft: #c8e38a;
    --berry-light: #f0a8a8;
    --berry: #d97c80;
    --berry-deep: #a55a6a;
    --waffle-light: #e0a45a;
    --waffle: #c27a33;
    --waffle-deep: #8e5322;
    --cup-cream: #efe7dc;
    --cup-choc: #9a5a3a;
  }
  html, body {
    margin: 0;
    padding: 0;
    width: 846px;
    height: 1200px;
    overflow: hidden;
    background: var(--paper);
  }
  .poster {
    position: relative;
    width: 846px;
    height: 1200px;
    background: var(--paper);
  }
  .poster__art {
    position: absolute;
    inset: 0;
  }
  .brand {
    position: absolute;
    left: 0;
    width: 846px;
    top: 480px;
    margin: 0;
    text-align: center;
    font-family: "Rubik", sans-serif;
    font-weight: 800;
    font-size: 132px;
    line-height: 1;
    letter-spacing: 4px;
    color: var(--paper);
  }
  .tagline {
    position: absolute;
    left: 0;
    width: 846px;
    top: 640px;
    margin: 0;
    text-align: center;
    font-family: "Rubik", sans-serif;
    font-weight: 800;
    font-size: 44px;
    line-height: 1;
    letter-spacing: 1px;
    color: var(--ink);
  }
  .price-symbol {
    position: absolute;
    left: 460px;
    top: 250px;
    font-family: "Rubik", sans-serif;
    font-weight: 800;
    font-size: 68px;
    line-height: 1;
    color: var(--lime-soft);
  }
  .cup-label {
    position: absolute;
    font-family: "Rubik", sans-serif;
    font-weight: 800;
    color: var(--leaf);
    line-height: 1;
    white-space: nowrap;
  }
  .cup-label--volume {
    left: 150px;
    top: 862px;
    font-size: 36px;
    transform: rotate(42deg);
  }
  .cup-label--spoon {
    left: 548px;
    top: 842px;
    font-size: 33px;
    transform: rotate(-45deg);
  }
</style>
</head>
<body>
<main class="poster">
  <svg class="poster__art" width="846" height="1200" viewBox="0 0 846 1200" xmlns="http://www.w3.org/2000/svg">
    <defs>
      <clipPath id="disc-clip">
        <circle cx="430" cy="588" r="405"/>
      </clipPath>
      <linearGradient id="scoop-tone" x1="0" y1="0" x2="0.3" y2="1">
        <stop offset="0" stop-color="var(--berry-light)"/>
        <stop offset="0.6" stop-color="var(--berry)"/>
        <stop offset="1" stop-color="var(--berry-deep)"/>
      </linearGradient>
      <linearGradient id="waffle-tone" x1="0" y1="0" x2="0.4" y2="1">
        <stop offset="0" stop-color="var(--waffle-light)"/>
        <stop offset="0.55" stop-color="var(--waffle)"/>
        <stop offset="1" stop-color="var(--waffle-deep)"/>
      </linearGradient>
      <radialGradient id="cup-tone" cx="0.5" cy="0.55" r="0.5">
        <stop offset="0" stop-color="var(--cup-choc)"/>
        <stop offset="0.6" stop-color="var(--cup-cream)"/>
        <stop offset="1" stop-color="#d9cfc2"/>
      </radialGradient>
    </defs>

    <g class="disc" clip-path="url(#disc-clip)">
      <rect class="disc__scoop" role="img" aria-label="Close-up photo of a scoop of strawberry ice cream" x="0" y="170" width="846" height="408" fill="url(#scoop-tone)"/>
      <rect class="disc__waffle" role="img" aria-label="Close-up photo of a golden waffle cone" x="0" y="576" width="846" height="420" fill="url(#waffle-tone)"/>
    </g>

    <path class="price-spot" d="M419 188 C470 186 512 214 520 258 C532 300 514 350 482 378 C452 404 400 408 366 388 C330 366 314 322 320 280 C326 230 366 190 419 188 Z"
      fill="var(--paper)" stroke="var(--lime-soft)" stroke-width="7"/>

    <path class="flavour-splash__shadow" d="M420 412 C486 410 548 448 560 508 C574 566 566 640 548 690 C530 740 480 770 420 768 C360 766 302 730 284 676 C264 616 266 546 288 494 C312 440 362 414 420 412 Z"
      fill="var(--lime-soft)"/>
    <path class="flavour-splash" d="M416 424 C478 420 538 456 552 514 C566 570 560 640 540 690 C520 738 474 760 416 758 C356 756 306 726 290 672 C274 614 272 548 294 498 C318 446 360 428 416 424 Z"
      fill="var(--leaf)"/>

    <path class="cup-window" role="img" aria-label="Photo of an open ice cream cup with a wooden spoon"
      d="M420 770 C468 768 508 790 520 832 C532 874 522 920 496 948 C468 974 418 980 378 962 C342 944 322 904 326 860 C330 812 370 772 420 770 Z"
      fill="url(#cup-tone)" stroke="var(--lime-soft)" stroke-width="6"/>
  </svg>

  <div class="price-symbol">$</div>

  <h1 class="brand">KELBURN</h1>
  <p class="tagline">Fine ice cream</p>

  <span class="cup-label cup-label--volume">125 ml</span>
  <span class="cup-label cup-label--spoon">spoon icluded</span>
</main>
</body>
</html>
```